Etiketten für Honiggläser
Zielgruppe
Ich bin ein Imker und möchte meinen Honig verkaufen.
Aufgabenstellung
Ich möchte exklusive und edle Honigetiketten die auffallen. Ich habe weder ein Logo noch hat meine Imkerei einen Namen. ( Vorschläge sind aber auch willkommen ).
Auf die Vorderseite des Honigetiketts soll zu lesen sein:
- Deutscher Honig
- Art des Honigs: Blütenhonig / Waldhonig ...
- 500g
Auf der Rückseite des Honigetiketts soll zu finden sein:
- Namen und Adresse des Imkers
- freies Feld für das Mindesthaltbarkeitsdatum
Ergänzende Informationen:
- Name: Tobias Wend
- Adresse: Lindauer Gasse 47, 85399 Eggmoos ( Bayern )
Bitte in einem Format liefern, dass ich ohne Aufwände an eine Druckerei übergeben kann. Außerdem muss ich die Dateien bearbeiten können in Photoshop o.ä. um zB die Art des Honigs und die Füllmenge anpassen zu können.
Wichtig:
Die Abmessungen des Labels sollen 15,5cm - 17cm breit und 6cm hoch sein.

```html
<!DOCTYPE html>
<html lang="de">
<head>
<meta charset="utf-8">
<title>Honigetikett – Rückseite und Vorderseite</title>
<link rel="stylesheet" href="https://fonts.googleapis.com/css2?family=Sniglet&family=Parisienne&family=PT+Sans:ital,wght@0,400;1,400;1,700&display=swap">
<style>
  :root {
    --page: #ffffff;
    --label-bg: #f6f6f6;
    --gold: #e9d57a;
    --gold-deep: #d8c257;
    --gold-light: #f2e49c;
    --blush: #f6dcd0;
    --blush-text: #fdf0ea;
    --script-pink: #f4cbbd;
    --mint: #dcedc4;
    --rose: #f3dcda;
    --sand: #efe6c6;
    --sky: #d5e3f6;
    --lavender: #ddd8e9;
    --salmon: #eb9f78;
    --blue-text: #7eaae2;
    --white: #ffffff;
  }
  * { box-sizing: border-box; margin: 0; padding: 0; }
  html, body {
    width: 1200px; height: 1159px; overflow: hidden;
    background: var(--page);
  }
  .label {
    position: absolute; left: 60px; top: 186px;
    width: 1080px; height: 786px;
    background: var(--label-bg);
    overflow: hidden;
    border-top: 6px solid var(--gold);
    border-bottom: 8px solid var(--gold);
  }
  .block { position: absolute; }

  .heading-band {
    left: 0; top: 21px; width: 478px; height: 116px;
    background: var(--blush);
    display: flex; align-items: center; justify-content: center;
  }
  .heading {
    font-family: "Sniglet", system-ui, sans-serif; font-weight: 400;
    font-size: 40px; line-height: 1; letter-spacing: 3px;
    color: var(--blush-text); white-space: nowrap;
  }
  .variety-panel {
    left: 0; top: 137px; width: 478px; height: 327px;
    background: linear-gradient(180deg, var(--gold-deep) 0%, var(--gold-light) 60%, var(--gold-deep) 100%);
  }
  .variety {
    position: absolute; left: 0; right: 0; top: 50px;
    text-align: center;
    font-family: "Parisienne", cursive; font-weight: 400;
    font-size: 88px; line-height: 1.2;
    color: var(--script-pink); white-space: nowrap;
  }
  .weight {
    position: absolute; right: 36px; bottom: 28px;
    font-family: "PT Sans", sans-serif; font-style: italic; font-weight: 700;
    font-size: 44px; line-height: 1; letter-spacing: 1.5px;
    color: var(--white);
  }
  .art { position: absolute; }

  .address-frame {
    left: 571px; top: 127px; width: 467px; height: 499px;
    border: 23px solid var(--gold);
    background: var(--gold-light);
  }
  .address-box {
    position: absolute; left: 4px; top: 12px; right: 4px; height: 219px;
    background: var(--white);
    padding: 20px 0 0 22px;
    font-family: "PT Sans", sans-serif; font-style: italic; font-weight: 700;
    font-size: 42px; line-height: 61px; letter-spacing: 1px;
    color: var(--salmon); white-space: nowrap;
  }
  .date-box {
    position: absolute; left: 4px; top: 269px; right: 4px; height: 174px;
    background: #f1f5fb;
    padding: 10px 0 0 12px;
  }
  .date-box p {
    font-family: "PT Sans", sans-serif; font-weight: 400;
    font-size: 25px; color: var(--blue-text);
  }
  .sky-block {
    left: 571px; top: 626px; width: 245px; height: 71px;
    background: var(--sky);
  }
</style>
</head>
<body>
<main class="label" aria-label="Honigetikett">
  <svg class="art" width="1080" height="786" viewBox="0 0 1080 786">
    <polygon points="0,404 461,578 403,772 0,772" fill="var(--mint)" role="img" aria-label="Illustration: Schale mit Honigwaben und Gänseblümchen"/>
    <rect x="691" y="0" width="389" height="271" fill="var(--rose)" role="img" aria-label="Illustration: Biene"/>
    <rect x="803" y="322" width="277" height="450" fill="var(--lavender)" role="img" aria-label="Illustration: Bienenstock"/>
    <rect x="500" y="28" width="150" height="145" fill="var(--sand)" transform="rotate(-10 575 100)" role="img" aria-label="Illustration: Kleeblüte"/>
    <rect x="920" y="95" width="150" height="150" fill="none" stroke="var(--white)" stroke-width="14"/>
    <rect x="935" y="108" width="122" height="125" fill="var(--gold-light)" opacity="0.6"/>
  </svg>

  <section class="block heading-band">
    <h1 class="heading">DEUTSCHER HONIG</h1>
  </section>
  <section class="block variety-panel">
    <h2 class="variety">Blütenhonig</h2>
    <p class="weight">500g</p>
  </section>

  <section class="block address-frame">
    <address class="address-box">Tobias Wend<br>Lindauer Gasse 47,<br>85399 Eggmoos</address>
    <div class="date-box"><p>mindesthaltbarkeitsdatum:</p></div>
  </section>
  <div class="block sky-block"></div>
</main>
</body>
</html>
```